company profile catalogue for Architecture and Interior Design and project management company

We target private customers who want to design a villa or a residential palace. We also target international brands, restaurants, furniture stores and malls.

Our logo on the front page.
Simple but inviting and professional.
The goal is to convey to the customer that we are professional design professionals and professional contractors.
And accuracy in action.
And commitment to the duration of the project.

We are Architectural and Interior design firm and we want a company profile catalogue which has the following:

Three sections with a small difference in theme (in colors) which demo the following
(It contains a group of projects with photos with a description for each photo included) :
A- (Architectural design)
B- (Interior design)
C- (Contracting and Project management)

We want only (7) pages to be designed, which will contain the following:
1- Front Cover page
2- Back cover page
3- Introduction page (Text & 1 Picture)
4- Document page (contain also text w/o 1 picture)
5&6&7- Three pages (which will contain pictures for project and should be flexible, their scheme as following:)
• Contain 1 picture with text
• Contain 2 pictures with text
• Contain 3 pictures with text

Notes:
1- The catalog structure guide also included
2- We have attached our current profile so you can take an idea how the main structure of the catalog (87MB):
https://www.filecrate-example.net/s/qmra82pzk4lwtcn/k%26mprofile2017-rev1.1.pdf?dl=0
3- We also attached the logo of our firm

Target Market(s)

Industry/Entity Type

Architecture

Font styles to use
Serif

Requirements
Must have
• Our logo on the front page.
• Simple but inviting and professional.
• The goal is to convey to the customer that we are professional design professionals and professional contractors.
• And accuracy in action.
• And commitment to the duration of the project.
Nice to have
• Our logo and The distinctive colors of each department
Should not have
• Should not use anything from the previous design, we are looking for something new and elegant.

```html
<!DOCTYPE html>
<html lang="en">
<head>
<meta charset="utf-8">
<title>Company Profile – Interior Spread</title>
<link href="https://fonts.googleapis.com/css2?family=Lato:wght@300;400&display=swap" rel="stylesheet">
<style>
  :root {
    --backdrop: #a3a3a3;
    --paper: #ffffff;
    --paper-shade: #f1f1f1;
    --band-dark: #0d4f94;
    --band-light: #2273c4;
    --accent-soft: #6d97c7;
    --accent-deep: #3f7cc0;
    --ink: #6b6b6b;
    --caption-ink: #8a8a8a;
    --photo-warm: #c9b79c;
    --photo-deep: #8b7458;
    --photo-cool: #a7b6a3;
  }
  * { box-sizing: border-box; margin: 0; padding: 0; }
  html, body { width: 1200px; height: 900px; overflow: hidden; }
  body {
    background: var(--backdrop);
    font-family: "Lato", sans-serif;
    position: relative;
  }
  .spread {
    position: absolute;
    left: 60px; top: 257px;
    width: 1080px; height: 385px;
    display: flex;
    box-shadow: 0 10px 30px rgba(0,0,0,0.25);
  }
  .page {
    position: relative;
    width: 540px; height: 385px;
    background: var(--paper);
    overflow: hidden;
  }
  .page--left { background: linear-gradient(to right, var(--paper) 88%, var(--paper-shade)); }
  .page--right { background: linear-gradient(to left, var(--paper) 88%, var(--paper-shade)); }

  .section-band {
    position: absolute;
    left: 0; top: 78px;
    width: 362px; height: 50px;
    background: linear-gradient(to right, var(--band-dark) 55%, var(--band-light));
    color: #fff;
    font-weight: 300;
    font-size: 19px;
    letter-spacing: 0.3px;
    display: flex; align-items: center;
    padding-left: 170px;
  }
  .body-columns {
    position: absolute;
    left: 108px; top: 180px;
    width: 340px;
    display: flex; gap: 24px;
  }
  .body-columns p {
    flex: 1;
    font-size: 7.6px;
    line-height: 11.6px;
    color: var(--ink);
    text-align: justify;
    height: 175px;
    overflow: hidden;
  }

  .photo {
    position: absolute;
    border-radius: 1px;
  }
  .photo--hall { left: 22px; top: 40px; width: 300px; height: 148px;
    background: linear-gradient(160deg, #efe4cf, var(--photo-warm) 50%, var(--photo-deep)); }
  .photo--sitting { left: 55px; top: 238px; width: 250px; height: 118px;
    background: linear-gradient(170deg, #4e5b57, var(--photo-cool) 45%, var(--photo-warm) 80%, var(--photo-deep)); }
  .photo--gallery { left: 312px; top: 200px; width: 220px; height: 124px;
    background: linear-gradient(180deg, #ede3d2, var(--photo-warm) 60%, var(--photo-deep)); }

  .caption {
    position: absolute;
    font-size: 5.6px;
    line-height: 7.6px;
    color: var(--caption-ink);
  }
  .caption--hall { left: 22px; top: 192px; width: 300px; }
  .caption--sitting { left: 55px; top: 360px; width: 250px; }
  .caption--gallery { left: 312px; top: 328px; width: 220px; }

  .tab-bar {
    position: absolute;
    left: 470px; top: 0;
    width: 30px; height: 68px;
    background: var(--accent-soft);
  }
  .tab-square {
    position: absolute;
    left: 478px; top: 110px;
    width: 24px; height: 20px;
    background: var(--accent-deep);
  }
</style>
</head>
<body>
  <main class="spread">
    <section class="page page--left">
      <h2 class="section-band">Fugitasp ienditium</h2>
      <div class="body-columns">
        <p>Every project begins with listening. Our architects and interior designers sit with each client to understand how a home, a restaurant or a store should feel, work and grow over time. From the first sketch to the final handover, one dedicated team carries the design, the drawings, the approvals and the site work, so nothing is lost between stages. We plan each phase in detail, agree clear milestones and report progress openly, keeping budgets and timelines firmly in view. Villas, private palaces, retail interiors and hospitality spaces all receive the same care and precision.</p>
        <p>Our contracting division turns approved designs into finished spaces. Skilled site managers coordinate trusted craftsmen, suppliers and consultants, checking every detail against the drawings. Materials are chosen for beauty and durability, and every finish is inspected before it is signed off. International brands rely on us to open stores and restaurants on schedule, while private owners trust us with homes built to last for generations. Commitment to the agreed duration is part of every contract we sign, and accuracy in action is how we keep it. We deliver spaces that are calm and elegant.</p>
      </div>
    </section>

    <section class="page page--right">
      <div class="tab-bar"></div>
      <div class="tab-square"></div>

      <div class="photo photo--hall" role="img" aria-label="Interior view of a palace reception hall with lounge seating and ceiling lights"></div>
      <p class="caption caption--hall">Main reception hall of a private residential palace, with layered ceiling lighting, panelled walls and a central lounge arranged for family gatherings and guests.</p>

      <div class="photo photo--sitting" role="img" aria-label="Formal sitting room with sage sofas, cream armchair and round coffee table"></div>
      <p class="caption caption--sitting">Formal sitting room in soft sage and cream tones, with a sculpted coffee table and tall timber doors leading to the dining wing.</p>

      <div class="photo photo--gallery" role="img" aria-label="Double-height gallery with crystal chandelier and curved balconies"></div>
      <p class="caption caption--gallery">Double-height gallery with a crystal chandelier and curved balconies, designed and delivered within the agreed project duration.</p>
    </section>
  </main>
</body>
</html>
```